Steady Harbor Leadership Roundtable Series Promotion

I'm wanting a single page (for now) website to promote my leadership training. Content would include: basic messaging what Steady Harbor means, invitation to join the Steady Harbor Roundtable workshops, have me come speak to them, join me on a leadership getaway, get personal coaching, watch some video links of Rud, then referrals of people saying nice things about Rud, connect to Rud’s personal website to learn more about me. The goal of the page is to 1) get people excited to attend a workshop, hear me speak, coach them, or join me on a getaway trip, 2) educate them in how they can get in control of their own life, and 3) link to my personal site to learn more about me. This is the general idea: https://www.perlwickstand.com/

Target Market(s)

Business owners or self improvement enthusiasts looking to take their businesses and personal lives to the next level.

Industry/Entity Type

Business Consultant

Coding

Coded - Design and coding required

Number of Pages Required

1 page

Font styles to use
Other font styles liked:
• See uploaded logo

Colors
0392cd

Requirements
Must have
• Fonts and colors that match the logo that was uploaded. Uplifting, inspirational look and feel.
Nice to have
• Similar to: https://www.perlwickstand.com/ and https://dorvankessling.com/

```html
<!DOCTYPE html>
<html lang="en">
<head>
<meta charset="utf-8">
<title>Steady Harbor Roundtable</title>
<link href="https://fonts.googleapis.com/css2?family=Cinzel:wght@400;600&family=Oswald:wght@500&family=Lato:ital,wght@0,400;0,700;1,400&display=swap" rel="stylesheet">
<style>
:root{
  --blue:#37bdec;
  --blue-soft:rgba(255,255,255,.12);
  --ink:#111;
  --text:#555;
  --grey-band:#f4f4f4;
  --black:#000;
  --white:#fff;
}
*{margin:0;padding:0;box-sizing:border-box}
html,body{width:1200px;height:3906px;overflow:hidden}
body{position:relative;background:var(--white);font-family:'Lato',sans-serif;color:var(--text)}
.abs{position:absolute}
.serif{font-family:'Cinzel',serif}
.btn{position:absolute;display:flex;align-items:center;justify-content:center;background:var(--blue);color:var(--ink);font-family:'Cinzel',serif;font-size:20px;letter-spacing:.5px;text-decoration:none}

.topbar{left:0;top:0;width:1200px;height:41px;background:var(--black);color:var(--white);font-size:15px}
.topbar .phone{left:77px;top:11px;display:flex;align-items:center;gap:10px}
.topbar .divider{left:232px;top:11px;width:1px;height:19px;background:#888}
.topbar .dot{top:14px;width:13px;height:13px;border-radius:50%;background:var(--white)}
.topbar .login{right:78px;top:11px;display:flex;align-items:center;gap:10px;font-weight:700}

.nav{left:0;top:41px;width:1200px;height:94px;background:var(--white)}
.brand{left:77px;top:26px;font-family:'Cinzel',serif;font-weight:600;font-size:22px;color:var(--ink);line-height:1;display:flex;align-items:center;gap:8px}
.brand .mark{width:12px;height:12px;border-radius:50%;background:var(--blue)}
.brand small{display:block;font-size:11px;letter-spacing:4px;margin-top:4px;font-weight:400}
.menu{right:118px;top:40px;display:flex;gap:27px;font-size:13px;color:#555;letter-spacing:.3px}
.search{right:78px;top:37px}

.hero{left:0;top:135px;width:1200px;height:563px;background:radial-gradient(ellipse at 55% 40%,#4c4c4c 0%,#2a2a2a 55%,#1d1d1d 100%)}
.hero h1{position:absolute;left:0;width:1200px;top:170px;text-align:center;font-family:'Oswald',sans-serif;font-weight:500;font-size:84px;color:var(--blue);letter-spacing:1px;line-height:1}
.hero p{position:absolute;left:0;width:1200px;top:282px;text-align:center;color:var(--white);font-size:19px}
.hero .btn{left:506px;top:340px;width:188px;height:52px}

.join{left:0;top:698px;width:1200px;height:207px;background:var(--grey-band)}
.join h2{position:absolute;left:79px;top:44px;font-family:'Cinzel',serif;font-weight:400;font-size:27px;color:var(--ink);line-height:38px;width:680px}
.join p{position:absolute;left:79px;top:134px;font-size:13.5px}
.join .btn{left:935px;top:84px;width:188px;height:52px}

.section-title{position:absolute;left:0;width:1200px;text-align:center;font-family:'Cinzel',serif;font-weight:400;font-size:40px;color:var(--ink)}
.section-text{position:absolute;left:200px;width:800px;text-align:center;font-size:14px;line-height:25px}

.card{position:absolute;width:333px;height:249px;background:linear-gradient(160deg,#5a5a5a,#262626)}
.card span{position:absolute;left:0;width:100%;top:155px;text-align:center;color:var(--white);font-family:'Cinzel',serif;font-size:19px;line-height:29px;padding:0 30px}

.video{left:77px;top:1696px;width:478px;height:312px;background:linear-gradient(120deg,#6a3a2a 0%,#553858 35%,#2b3a6a 70%,#2a2a3a 100%)}
.video svg{position:absolute;left:199px;top:116px}
.video-copy{left:660px;top:1714px;width:462px;font-size:14px;line-height:25px}
.video-copy p+p{margin-top:15px}

.stories{left:0;top:2093px;width:1200px;height:604px;background:var(--blue)}
.stories h2{position:absolute;left:0;width:1200px;top:58px;text-align:center;font-family:'Cinzel',serif;font-weight:400;font-size:40px;color:var(--white)}
.stories .panel{left:438px;top:179px;width:323px;height:311px;background:var(--blue-soft)}
.stories .avatar{left:556px;top:133px;width:88px;height:88px;border-radius:50%;background:linear-gradient(#d9c9c0,#7a5c4e);border:3px solid var(--white)}
.stories .quote{left:583px;top:250px}
.stories blockquote{position:absolute;left:320px;width:560px;top:304px;text-align:center;color:var(--white);font-style:italic;font-size:18px;line-height:29px}
.stories .name{left:0;width:1200px;top:410px;text-align:center;color:var(--white);font-size:20px}
.stories .dots{left:572px;top:516px;display:flex;gap:6px}
.stories .dots i{width:14px;height:14px;border-radius:50%;background:rgba(255,255,255,.35)}
.stories .dots i:first-child{background:var(--white)}

.visit{left:0;top:3270px;width:1200px;height:188px;background:var(--blue)}
.visit h2{position:absolute;left:79px;top:57px;font-family:'Cinzel',serif;font-weight:400;font-size:26px;color:var(--white);letter-spacing:.5px}
.visit a.link{position:absolute;left:79px;top:109px;color:var(--white);font-style:italic;font-size:18px}
.visit .btn{left:936px;top:76px;width:187px;height:52px;background:var(--white);color:var(--blue)}

.footer{left:0;top:3458px;width:1200px;height:448px;background:var(--black);color:var(--white);font-size:14px;line-height:25px}
.footer h3{font-family:'Cinzel',serif;font-weight:400;font-size:19px;color:var(--blue);line-height:29px;letter-spacing:.5px}
.footer .col{position:absolute;top:69px}
.footer .col p{margin-top:12px}
.footer .sitemap{display:grid;grid-template-columns:186px 150px;row-gap:15px;margin-top:20px}
.footer .social{display:flex;gap:26px;margin-top:20px}
.footer .social i{width:15px;height:15px;border-radius:50%;background:var(--white)}
.footer .rule{left:77px;top:376px;width:1046px;height:1px;background:#333}
.footer .copy{left:0;width:1200px;top:398px;text-align:center;font-size:13px}
.footer .copy span{font-family:'Cinzel',serif;color:var(--blue)}
</style>
</head>
<body>

<div class="abs topbar">
  <div class="abs phone">
    <svg width="17" height="17" viewBox="0 0 24 24"><path fill="#37bdec" d="M6.6 10.8a15 15 0 0 0 6.6 6.6l2.2-2.2a1 1 0 0 1 1-.25 11.4 11.4 0 0 0 3.6.57 1 1 0 0 1 1 1V20a1 1 0 0 1-1 1A17 17 0 0 1 3 4a1 1 0 0 1 1-1h3.5a1 1 0 0 1 1 1c0 1.25.2 2.45.57 3.57a1 1 0 0 1-.25 1z"/></svg>
    <span>123-456-7890</span>
  </div>
  <div class="abs divider"></div>
  <div class="abs dot" style="left:257px"></div>
  <div class="abs dot" style="left:293px"></div>
  <div class="abs login">
    <svg width="16" height="17" viewBox="0 0 16 17"><circle cx="8" cy="4.5" r="4" fill="#37bdec"/><path d="M0 17c0-5 3.5-7 8-7s8 2 8 7z" fill="#37bdec"/></svg>
    <span>LOGIN</span>
  </div>
</div>

<header class="abs nav">
  <div class="abs brand"><span class="mark"></span><div>STEADY HARBOR<small>ROUNDTABLE</small></div></div>
  <nav class="abs menu"><span>WORKSHOP</span><span>VIDEO</span><span>ABOUT ME</span><span>COACHING</span><span>JOIN ME</span><span>RESOURCES</span></nav>
  <svg class="abs search" width="20" height="20" viewBox="0 0 20 20"><circle cx="8" cy="8" r="6" fill="none" stroke="#111" stroke-width="2.5"/><path d="M12.5 12.5 18 18" stroke="#111" stroke-width="2.8" stroke-linecap="round"/></svg>
</header>

<section class="abs hero" role="img" aria-label="Photo of a smiling speaker seated in a modern office, darkened behind the headline">
  <h1>GET CONTROL OF YOUR OWN LIFE</h1>
  <p>LOREM IPSUM IS SIMPLY DUMMY TEXT OF HGT BINNY GET IT OF SINE LIFE TIME OF ANND OF.</p>
  <a class="btn" href="#">START HERE</a>
</section>

<section class="abs join">
  <h2>Join the Steady Harbor Roundtable workshops Now</h2>
  <p>Lorem ipsum dolor sit amet, consectetur adipiscing elit, sed do eiusmod tempor incididunt ut labore.</p>
  <a class="btn" href="#">JOIN NOW</a>
</section>

<h2 class="section-title" style="top:948px">About Steady Harbor</h2>
<p class="section-text" style="top:1016px">Lorem ipsum dolor sit amet, consectetur adipiscing elit, sed do eiusmod tempor incididunt ut labore et dolore magna aliqua. Ut enim ad minim veniam, quis nostrud exercitation ullamco laboris nisi ut aliquip ex ea commodo consequat. Duis aute irure dolor in reprehenderit in voluptate velit esse cillum dolore eu fugiat nulla pariatur. Excepteur sint occaecat cupidatat non proident, sunt in culpa qui officia deserunt mollit anim id est laborum</p>

<div class="card" style="left:77px;top:1184px" role="img" aria-label="Photo of the speaker in a suit"><span>Have me come speak</span></div>
<div class="card" style="left:434px;top:1184px" role="img" aria-label="Photo of smiling colleagues in business attire"><span>Join me on a leadership getaway</span></div>
<div class="card" style="left:789px;top:1184px" role="img" aria-label="Photo of a team meeting around a table"><span>Get personal coaching</span></div>

<h2 class="section-title" style="top:1524px">Driven by purpose</h2>
<p class="section-text" style="top:1588px;left:260px;width:680px">Lorem ipsum dolor sit amet, consectetur adipiscing elit, sed do eiusmod tempor incididunt ut labore et dolore magna aliqua. Ut enim ad minim veniam, quis nostrud exercitation ullamco laboris nisi ut.</p>

<div class="abs video" role="img" aria-label="Video still of the speaker at a conference podium">
  <svg width="80" height="80" viewBox="0 0 80 80"><circle cx="40" cy="40" r="37" fill="none" stroke="#fff" stroke-width="4"/><circle cx="40" cy="40" r="29" fill="none" stroke="#fff" stroke-width="2"/><path d="M32 26 56 40 32 54z" fill="none" stroke="#fff" stroke-width="3" stroke-linejoin="round"/></svg>
</div>
<div class="abs video-copy">
  <p>Lorem ipsum dolor sit amet, consectetur adipiscing elit, sed do eiusmod tempor incididunt ut labore et dolore magna aliqua. Ut enim ad minim veniam, quis nostrud exercitation ullamco laboris nisi ut aliquip ex ea commodo consequat.</p>
  <p>Duis aute irure dolor in reprehenderit in voluptate velit esse cillum dolore eu fugiat nulla pariatur. Excepteur sint occaecat cupidatat non proident, sunt in culpa qui officia deserunt mollit anim id est laborum.</p>
</div>
<a class="btn" href="#" style="left:660px;top:1929px;width:187px;height:52px">WATCH MORE</a>

<section class="abs stories">
  <h2>Success Stories</h2>
  <div class="abs panel"></div>
  <div class="abs avatar" role="img" aria-label="Portrait photo of a client"></div>
  <svg class="abs quote" width="34" height="26" viewBox="0 0 34 26"><path fill="#fff" d="M0 26V14C0 6 4 1 12 0l1 4c-4 1-6 4-6 8h6v14zm20 0V14c0-8 4-13 12-14l1 4c-4 1-6 4-6 8h6v14z"/></svg>
  <blockquote>Lorem ipsum dolor sit amet, consectetur adipiscing elit, sed do eiusmod tempor incididunt ut labore et dolore magna aliqua. Ut enim ad minim veniam, quis nostrud exercitation</blockquote>
  <div class="abs name">Name surname</div>
  <div class="abs dots"><i></i><i></i><i></i></div>
</section>

<h2 class="section-title" style="top:2750px">Read, Watch, Listen</h2>
<p class="section-text" style="top:2813px;left:260px;width:680px">Lorem ipsum dolor sit amet, consectetur adipiscing elit, sed do eiusmod tempor incididunt ut labore et dolore magna aliqua. Ut enim ad minim veniam, quis nostrud exercitation ullamco laboris nisi ut.</p>

<div class="card" style="left:77px;top:2927px;background:linear-gradient(160deg,#6a6660,#2a2724)" role="img" aria-label="Photo of a presenter leading a workshop"><span style="top:166px">Attend a workshop</span></div>
<div class="card" style="left:434px;top:2927px;background:linear-gradient(160deg,#5a3a34,#2a2220)" role="img" aria-label="Photo of the speaker in a workshop hall"><span style="top:166px">Watch videos</span></div>
<div class="card" style="left:789px;top:2927px;background:linear-gradient(160deg,#3a3a4a,#6a3a34)" role="img" aria-label="Photo of an audience at a conference"><span style="top:166px">Hear me speak</span></div>

<section class="abs visit">
  <h2>Visit My Personal Site to Learn More About Me</h2>
  <a class="link" href="#">www.steadyharbor.com</a>
  <a class="btn" href="#">VISIT NOW</a>
</section>

<footer class="abs footer">
  <div class="col" style="left:79px;width:300px">
    <h3>Steady Harbor Roundtable</h3>
    <p>Lorem ipsum dolor sit amet, consectetur adipiscing elit, sed do eiusmod tempor.</p>
    <h3 style="margin-top:38px">Connect with Rud</h3>
    <div class="social"><i></i><i></i><i></i><i></i><i></i><i></i></div>
  </div>
  <div class="col" style="left:443px">
    <h3>Sitemap</h3>
    <div class="sitemap"><span>Workshop</span><span>Join me</span><span>Videos</span><span>Resources</span><span>About me</span><span>Terms</span><span>Coaching</span><span>Blog Post</span></div>
  </div>
  <div class="col" style="left:801px;width:300px">
    <h3>Media Inquiries</h3>
    <p>Lorem ipsum dolor sit amet, consectetur adipiscing elit, sed do eiusmod tempor incididunt ut labore et dolore magna aliqua.</p>
    <h3 style="margin-top:22px">Customer Support</h3>
    <p>Lorem ipsum dolor sit amet, consectetur adipiscing elit, sed do eiusmod tempor.</p>
  </div>
  <div class="abs rule"></div>
  <div class="abs copy">©<span>Steady Harbor Roundtable</span>. 2019 - All Rights Reserved.</div>
</footer>

</body>
</html>
```